Store Front / Boutique Front window signage

I am looking to have a sign printed to stick on the glass of my new Kitchens Cabinets showroom. I already have a logo that I will include however this is the "Boutique" location so I am looking to have my logo incorporated for brand recognition but I do not want just my logo. I want something classy, minimalist with class. Maybe even old school or vintage in style. I will include my store front window sizes and a picture of the store front.

My thought is to take my logo small to moderate in size. Take away the "Cabinetry and Design" part and place that statement larger like this
"Joinery and Interiors Atelier"
My website is Brambleworthkitchens.com
window panes are as follows
left is 72 3/4" wide
right is 70" wide
height is 97 1/2"

I would like to see something not too large , across the two panes
Updates

I have been with work family , looking to choose the best created design and then modify to my liking

Target Market(s)

People !

Font styles to use
Decorative
Script
Other font styles liked:
• vintage , classic

Requirements
Must have
• Tasteful . Maybe logo and small strip along the bottom with a manufacturers logos.
Should not have
• Should not be too large, the signage is not intended to be seen from driving by , more for foot traffic

```html
<!DOCTYPE html>
<html lang="en">
<head>
<meta charset="utf-8">
<title>Joinery and Interiors Atelier – Window Sign</title>
<link rel="stylesheet" href="https://fonts.googleapis.com/css2?family=Cormorant+Garamond:wght@500&family=Arimo:wght@400&display=swap">
<style>
  :root {
    --paper-edge: #d9c6a4;
    --paper-mid: #efe4cc;
    --paper-light: #fbf8f1;
    --sheet-white: #ffffff;
    --rust: #c45f2c;
    --walnut: #5a3416;
    --ink: #000000;
    --panel-text: #ffffff;
    --ornament-tone: #d9a074;
  }
  html, body {
    margin: 0;
    padding: 0;
    overflow: hidden;
  }
  body {
    width: 895px;
    height: 1200px;
    background: var(--sheet-white);
  }
  .sign {
    position: relative;
    width: 895px;
    height: 1200px;
    overflow: hidden;
    background:
      radial-gradient(ellipse 62% 58% at 56% 52%, var(--sheet-white) 55%, var(--paper-light) 72%, var(--paper-mid) 88%, var(--paper-edge) 100%);
  }
  .frame-lines {
    position: absolute;
    inset: 0;
  }
  .corner-ornament {
    position: absolute;
    width: 112px;
    height: 140px;
    border-radius: 40%;
    background: radial-gradient(circle at 45% 50%, rgba(217,160,116,0.45), rgba(217,160,116,0) 70%);
  }
  .corner-ornament--top { left: 38px; top: 38px; }
  .corner-ornament--bottom { left: 38px; top: 1015px; }
  .title {
    position: absolute;
    left: 150px;
    width: 680px;
    top: 522px;
    margin: 0;
    text-align: center;
    font-family: "Cormorant Garamond", Georgia, serif;
    font-weight: 500;
    font-style: normal;
    font-size: 62px;
    line-height: 78px;
    color: var(--ink);
  }
  .cutout-panel {
    position: absolute;
    left: 139px;
    top: 824px;
    width: 702px;
    height: 262px;
    box-sizing: border-box;
    border: 1.5px solid var(--walnut);
    border-radius: 32px;
    background: var(--sheet-white);
  }
  .cutout-panel__sticker {
    position: absolute;
    left: 9px;
    top: 5px;
    right: 8px;
    bottom: 7px;
    box-sizing: border-box;
    border: 7px solid var(--rust);
    border-radius: 26px;
    background: var(--ink);
    display: flex;
    align-items: center;
    justify-content: center;
  }
  .cutout-panel__note {
    margin: 0;
    font-family: "Arimo", Arial, sans-serif;
    font-size: 21px;
    color: var(--panel-text);
    transform: translateY(-5px);
  }
</style>
</head>
<body>
  <main class="sign">
    <svg class="frame-lines" width="895" height="1200" viewBox="0 0 895 1200" aria-hidden="true">
      <g fill="none" stroke-width="1">
        <line x1="190" y1="44" x2="895" y2="44" stroke="var(--rust)"/>
        <line x1="154" y1="50" x2="895" y2="50" stroke="var(--walnut)"/>
        <line x1="173" y1="56" x2="895" y2="56" stroke="var(--rust)"/>
        <line x1="61" y1="179" x2="61" y2="1018" stroke="var(--rust)"/>
        <line x1="67" y1="155" x2="67" y2="1032" stroke="var(--walnut)"/>
        <line x1="73" y1="190" x2="73" y2="1012" stroke="var(--rust)" stroke-width="0.6"/>
        <line x1="190" y1="1127" x2="895" y2="1127" stroke="var(--rust)"/>
        <line x1="154" y1="1132" x2="895" y2="1132" stroke="var(--walnut)"/>
        <line x1="173" y1="1138" x2="895" y2="1138" stroke="var(--rust)"/>
      </g>
      <g fill="var(--walnut)">
        <circle cx="154" cy="50" r="2"/>
        <circle cx="67" cy="155" r="2"/>
        <circle cx="67" cy="1032" r="2"/>
        <circle cx="154" cy="1132" r="2"/>
      </g>
    </svg>

    <div class="corner-ornament corner-ornament--top" role="img" aria-label="Vintage swirl flourish ornament at the top-left corner of the frame"></div>
    <div class="corner-ornament corner-ornament--bottom" role="img" aria-label="Vintage swirl flourish ornament at the bottom-left corner of the frame"></div>

    <h1 class="title">Joinery and Interiors<br>Atelier</h1>

    <section class="cutout-panel">
      <div class="cutout-panel__sticker">
        <p class="cutout-panel__note">Balck area sticker to be cut off for backside display</p>
      </div>
    </section>
  </main>
</body>
</html>
```